依頼詳細
現在、お店のロゴはあります。既存のロゴを使用して、立て看板を新しくしたいと思っています。看板の入稿に必要なデザインをillustratorで作成して頂きたいと思います。
重視するポイントは、
1。概要、特徴にも記載しましたが2Fとわかること。
2.ワインはそうですが、お食事ができること。
3.現在使用しているロゴを看板の中心にもっていってワインと一目でわかるようにしたい
4.現在の立て看板がとてもカジュアルな為、店内の雰囲気とかなりギャップがあります。若年の方が立ち飲みバルや、居酒屋、カフェ等と間違えて誤って入ってこられることがたまにあります。お店の雰囲気がでるようなシンプルで雰囲気のあるデザインを希望します。看板製作会社が、完全データの支給を要求しているため、Adobe Illustratorアウトラインデータ Mac=8.0 Win=CSにて納品お願いします。
お店の雰囲気、現在の看板、ロゴなどは添付ファイル参照ください。
記載項目
店舗名、2F、ワインとお食事、今のロゴ。定番メニューのリスト、電話番号。席数。
希望イメージ
シンプル 複雑
単色 カラフル
暗い 明るい
日常 高級
遊び心 厳粛
未来的 伝統的
女性的 男性的
希望する色
白、ワインレッド系、ロゴに合わせたカラー
納品ファイル
• 高解像度JPG (.jpg)
• イラストレーター形式 (.ai)
補足説明
入口の間口が狭いために、看板に必ず2F+↑を記載していただきたいです。表、左上がり、裏、右上がりの☝をつけてほしいです。現在の立て看板ファイルを参照してください。
看板仕上がりサイズはW600×H900です。【画面有効サイズ】 W530×H830mmとなっています。内側に投光機を設置し、ライトアップされます。宜しくお願いいたします。
■ 選んだ理由

現在の問題点をクリアし、お店の雰囲気が看板一つで出ている所。

■ 提案者全員のお礼・コメント

修正等にご対応いただきまして誠にありがとうございました。今後も名刺の修正等依頼していくつもりですので機会がありましたら是非とも宜しくお願いいたします。

```html
<!DOCTYPE html>
<html lang="ja">
<head>
<meta charset="utf-8">
<title>VERREAU 立て看板</title>
<link rel="stylesheet" href="https://fonts.googleapis.com/css2?family=Noto+Sans+JP:wght@400;500;700&display=swap">
<style>
  :root {
    --frame: #4a4446;
    --paper: #ffffff;
    --wine: #b5162b;
    --ink: #2b2326;
    --beige-light: #f3e6d2;
    --beige-deep: #c79a62;
    --rule: #3a3335;
  }
  * { margin: 0; padding: 0; box-sizing: border-box; }
  html, body { width: 884px; height: 1200px; overflow: hidden; background: var(--paper); }
  .signboard {
    position: relative;
    width: 884px;
    height: 1200px;
    background: var(--paper);
    border: 6px solid var(--frame);
    font-family: "Noto Sans JP", sans-serif;
    color: var(--ink);
    overflow: hidden;
  }
  .signboard__wash {
    position: absolute;
    left: 0; top: 0;
    width: 872px; height: 1188px;
  }
  .tagline {
    position: absolute;
    top: 178px; left: 0; width: 100%;
    text-align: center;
    font-size: 38px;
    font-weight: 500;
    letter-spacing: 1px;
  }
  .tagline .accent { color: var(--wine); }
  .shop-name {
    position: absolute;
    top: 288px; left: 0; width: 100%;
    display: flex; align-items: center; justify-content: center;
    gap: 26px;
  }
  .shop-name__dot {
    width: 44px; height: 44px; border-radius: 50%;
    background: var(--wine);
  }
  .shop-name__text {
    font-size: 120px;
    font-weight: 700;
    color: var(--wine);
    letter-spacing: 6px;
    line-height: 1;
  }
  .seats {
    position: absolute;
    top: 500px; left: 0; width: 100%;
    display: flex; justify-content: space-between;
    padding: 0 80px;
  }
  .seats__item {
    font-size: 34px;
    font-weight: 500;
    padding: 0 14px 12px;
    border-bottom: 2px solid var(--rule);
    position: relative;
  }
  .seats__item::before, .seats__item::after {
    content: ""; position: absolute; bottom: -2px;
    width: 2px; height: 14px; background: var(--rule);
  }
  .seats__item::before { left: 0; }
  .seats__item::after { right: 0; }
  .seats__item:first-child { margin-left: 10px; }
  .menu {
    position: absolute;
    top: 672px; left: 0; width: 100%;
    list-style: none;
    text-align: center;
    font-size: 34px;
    font-weight: 500;
  }
  .menu li { line-height: 46px; }
  .menu li + li::before {
    content: ""; display: block;
    width: 12px; height: 12px; border-radius: 50%;
    background: var(--wine);
    margin: 0 auto 2px;
  }
  .floor-rule {
    position: absolute;
    top: 985px; left: 40px; right: 40px;
    height: 2px; background: var(--rule);
  }
  .floor {
    position: absolute;
    top: 1010px; left: 70px;
    display: flex; align-items: center; gap: 14px;
  }
  .floor__label {
    font-size: 104px; font-weight: 500;
    color: var(--wine); line-height: 1;
  }
  .info {
    position: absolute;
    top: 1012px; left: 480px;
    font-size: 27px;
    line-height: 38px;
    color: var(--ink);
  }
</style>
</head>
<body>
<div class="signboard">
  <svg class="signboard__wash" viewBox="0 0 872 1188" aria-hidden="true">
    <defs>
      <linearGradient id="wash" x1="0" y1="0" x2="0" y2="1">
        <stop offset="0" stop-color="#fbf5ec"/>
        <stop offset="0.45" stop-color="#f0dfc5"/>
        <stop offset="1" stop-color="#c79a62"/>
      </linearGradient>
    </defs>
    <path d="M0 940 C 180 760, 520 640, 872 600 L 872 1188 L 0 1188 Z" fill="url(#wash)"/>
  </svg>

  <p class="tagline"><span class="accent">ワイン</span>と<span class="accent">お食事</span>が楽しめるワインバー</p>

  <div class="shop-name">
    <span class="shop-name__dot"></span>
    <span class="shop-name__text">VERREAU</span>
  </div>

  <div class="seats">
    <span class="seats__item">カウンター 7席</span>
    <span class="seats__item">テーブル 10席</span>
  </div>

  <ul class="menu">
    <li>国産牛トリッパの煮込</li>
    <li>自家製レバーパテ</li>
    <li>季節のお魚のカルパッチョ</li>
    <li>季節の食材を使用したパスタ2種</li>
  </ul>

  <div class="floor-rule"></div>

  <div class="floor">
    <span class="floor__label">2F</span>
    <svg width="100" height="96" viewBox="0 0 100 96" aria-label="上り階段の矢印" role="img">
      <path d="M6 90 H36 V62 H62 V34 H94" fill="none" stroke="#2b2326" stroke-width="6"/>
      <path d="M40 46 L14 20 M14 20 V42 M14 20 H36" fill="none" stroke="#2b2326" stroke-width="6" stroke-linecap="round"/>
    </svg>
  </div>

  <div class="info">
    <p>18:00-24:00(L.O.23:00)</p>
    <p>TEL:090-4827-6315</p>
    <p>http://www.verreau-wine.com/</p>
  </div>
</div>
</body>
</html>
```